out of the box Business Card Design for a Manufacturer / Distributor

We are a manufarturer and distributor of products.
the company name is VORTANI (Pic attached)

the picture is NOT a must have on the business Card.

the Business Card should look really professional and/or special, so out of the box thinking is welcome.

there should be 2 Adresses on the Business Card for Main and Branch Office.
Email Adress, homepage, Name is required
NO Phone Number

Our working field:
Private Labeling
high Quality Production
direct distribution
warehousing
trademark registration
legal support

Main Office:
Kornblumenweg 14
08352 Hollbrach
Germany

Branch Office:
Daska Lane
Zarikot
Pakistan

Names:
Lukas Feldhaus (Owner)
Imran Qureshi (Owner)

Email:
lukas@vortani-example.com
imran@vortani-example.com

homepage:
vortani-example.com

Industry/Entity Type

Manufacturer Distributer

Contact Information for Business Card

Vortani

Requirements
Must have
• Names, both office Adresses, email, homepage
Should not have
• Phone Number

```html
<!DOCTYPE html>
<html lang="en">
<head>
<meta charset="utf-8">
<title>Vortani Business Card</title>
<link rel="stylesheet" href="https://fonts.googleapis.com/css2?family=Poppins:wght@400;500;600&family=Montserrat:wght@400&family=Open+Sans:wght@600&display=swap">
<style>
  :root {
    --page: #ffffff;
    --card: #2f2f2f;
    --ink: #ffffff;
    --ink-soft: #ececec;
  }
  * { margin: 0; padding: 0; box-sizing: border-box; }
  html, body { width: 1200px; height: 1200px; overflow: hidden; background: var(--page); }
  .card {
    position: absolute;
    left: 180px;
    width: 848px;
    height: 484px;
    background: var(--card);
    color: var(--ink);
    overflow: hidden;
  }
  .card--front { top: 106px; }
  .card--back { top: 617px; }
  .abs { position: absolute; white-space: nowrap; }

  .person-name {
    left: 79px; top: 94px;
    font: 600 40px/1 "Poppins", sans-serif;
    letter-spacing: 0.5px;
  }
  .person-role {
    left: 80px; top: 142px;
    font: 400 23px/1 "Poppins", sans-serif;
    letter-spacing: 0.6px;
  }
  .contact-email {
    left: 79px; top: 176px;
    display: flex; align-items: center; gap: 12px;
    font: 400 24px/1 "Poppins", sans-serif;
    letter-spacing: 0.4px;
  }
  .office { top: 274px; }
  .office--main { left: 76px; }
  .office--branch { left: 389px; }
  .office-title {
    display: flex; align-items: center; gap: 10px;
    font: 600 25px/1 "Open Sans", sans-serif;
    letter-spacing: 0.5px;
    margin-bottom: 6px;
  }
  .office-address {
    font: 400 22px/30px "Montserrat", sans-serif;
    color: var(--ink-soft);
    letter-spacing: 0.6px;
  }
  .office--branch .office-address { margin-top: 2px; }

  .brand-dot {
    left: 142px; top: 160px;
    width: 120px; height: 120px;
    border-radius: 50%;
    background: var(--ink);
  }
  .brand-name {
    left: 306px; top: 174px;
    font: 400 96px/1 "Poppins", sans-serif;
    letter-spacing: 2px;
  }
  .brand-site {
    left: 306px; top: 278px;
    font: 500 34px/1 "Poppins", sans-serif;
    letter-spacing: 1px;
  }
</style>
</head>
<body>
  <section class="card card--front">
    <h1 class="abs person-name">LUKAS FELDHAUS</h1>
    <p class="abs person-role">OWNER</p>
    <p class="abs contact-email">
      <svg width="20" height="15" viewBox="0 0 20 15" aria-hidden="true"><path d="M0 0h20v15H0z" fill="#fff"/><path d="M1 1l9 7 9-7" fill="none" stroke="#2f2f2f" stroke-width="2"/></svg>
      lukas@vortani-example.com
    </p>

    <div class="abs office office--main">
      <h2 class="office-title">
        <svg width="14" height="20" viewBox="0 0 14 20" aria-hidden="true"><path d="M7 0a7 7 0 0 0-7 7c0 5 7 13 7 13s7-8 7-13a7 7 0 0 0-7-7z" fill="#fff"/><circle cx="7" cy="7" r="2.6" fill="#2f2f2f"/></svg>
        MAIN OFFICE
      </h2>
      <p class="office-address">Kornblumenweg 14<br>08352 Hollbrach<br>Germany</p>
    </div>

    <div class="abs office office--branch">
      <h2 class="office-title">
        <svg width="14" height="20" viewBox="0 0 14 20" aria-hidden="true"><path d="M7 0a7 7 0 0 0-7 7c0 5 7 13 7 13s7-8 7-13a7 7 0 0 0-7-7z" fill="#fff"/><circle cx="7" cy="7" r="2.6" fill="#2f2f2f"/></svg>
        BRANCH OFFICE
      </h2>
      <p class="office-address">Daska Lane<br>Zarikot<br>Pakistan</p>
    </div>
  </section>

  <section class="card card--back">
    <span class="abs brand-dot" aria-hidden="true"></span>
    <p class="abs brand-name">VORTANI</p>
    <p class="abs brand-site">vortani-example.com</p>
  </section>
</body>
</html>
```